Brivora Collective Business Card Design

We need a business card design for Brivora Collective. We are a healthcare recruiting, wellness and education company. We partner with medical facilities to find quality candidates. We also offer free wellness courses.
The final design should communicate an emphasis on recruiting and wellness
The main purpose of the business card is to utilized it for networking events, give to hospitals, executives, VCs surgery centers and clinics. I want it to be sleek, clean, use of our brand colors and professional.

```html
<!DOCTYPE html>
<html lang="en">
<head>
<meta charset="utf-8">
<title>Brivora Collective – Business Card</title>
<link rel="stylesheet" href="https://fonts.googleapis.com/css2?family=Montserrat:wght@400;500;800&display=swap">
<style>
  :root {
    --stage: #2f2f30;
    --ink: #111515;
    --paper: #ffffff;
    --teal: #03574f;
    --deep: #0a1a1a;
    --rule: #2b2b2b;
  }
  * { box-sizing: border-box; margin: 0; padding: 0; }
  html, body { width: 1200px; height: 800px; overflow: hidden; }
  body {
    background: var(--stage);
    font-family: "Montserrat", Arial, sans-serif;
    display: flex;
    flex-direction: column;
    align-items: center;
    justify-content: center;
    gap: 36px;
  }
  .card {
    position: relative;
    width: 600px;
    height: 343px;
    overflow: hidden;
    box-shadow: 0 14px 30px rgba(0,0,0,.35);
  }
  .card-art { position: absolute; inset: 0; width: 100%; height: 100%; }

  /* Back */
  .card--back { background: var(--deep); }
  .back-brand {
    position: absolute;
    left: 150px; top: 132px;
    display: flex; align-items: center; gap: 14px;
    color: var(--teal);
    font-weight: 500;
    font-size: 34px;
    letter-spacing: -.5px;
  }
  .brand-mark { width: 22px; height: 22px; background: var(--teal); border-radius: 4px; }
  .back-url {
    position: absolute;
    left: 214px; top: 196px;
    color: var(--teal);
    font-size: 13px;
    letter-spacing: 1px;
  }

  /* Front */
  .card--front { background: var(--paper); }
  .front-brand {
    position: absolute;
    left: 34px; top: 150px;
    display: flex; align-items: center; gap: 10px;
    color: var(--teal);
    font-weight: 500;
    font-size: 24px;
    letter-spacing: -.3px;
  }
  .front-brand .brand-mark { width: 16px; height: 16px; border-radius: 3px; }
  .contact {
    position: absolute;
    left: 322px; top: 56px;
    color: var(--ink);
  }
  .contact-name { font-weight: 800; font-size: 18px; letter-spacing: .3px; }
  .contact-title { font-size: 13px; margin-bottom: 12px; }
  .contact-list { list-style: none; font-size: 13px; line-height: 1.55; }
  .contact-list li { display: flex; align-items: center; gap: 8px; }
  .contact-list svg { width: 12px; height: 12px; flex: none; }
  .contact-address { margin-top: 8px; font-size: 13px; line-height: 1.4; }
</style>
</head>
<body>

<section class="card card--back" aria-label="Business card back">
  <svg class="card-art" viewBox="0 0 600 343" aria-hidden="true">
    <line x1="600" y1="26" x2="470" y2="26" stroke="var(--teal)" stroke-width="1.5"/>
    <circle cx="470" cy="26" r="4" fill="var(--teal)"/>
    <line x1="0" y1="318" x2="170" y2="318" stroke="var(--teal)" stroke-width="1.5"/>
    <circle cx="170" cy="318" r="4" fill="var(--teal)"/>
  </svg>
  <div class="back-brand"><span class="brand-mark"></span>Brivora Collective</div>
  <p class="back-url">www.brivoracollective.com</p>
</section>

<section class="card card--front" aria-label="Business card front">
  <svg class="card-art" viewBox="0 0 600 343" aria-hidden="true">
    <line x1="300" y1="40" x2="300" y2="250" stroke="var(--rule)" stroke-width="1"/>
    <polygon points="580,0 600,0 600,252 580,258" fill="var(--deep)"/>
    <polygon points="110,343 600,343 600,262 560,268" fill="var(--teal)"/>
  </svg>
  <div class="front-brand"><span class="brand-mark"></span>Brivora Collective</div>
  <div class="contact">
    <h1 class="contact-name">YOUR NAME</h1>
    <p class="contact-title">Title here</p>
    <ul class="contact-list">
      <li>
        <svg viewBox="0 0 12 12"><path d="M2.5 1h2l1 3-1.3 1a6 6 0 0 0 2.8 2.8l1-1.3 3 1v2a1 1 0 0 1-1 1A10 10 0 0 1 1.5 2a1 1 0 0 1 1-1z" fill="var(--teal)"/></svg>
        123-456-789
      </li>
      <li>
        <svg viewBox="0 0 12 12"><rect x="0.5" y="2" width="11" height="8" fill="var(--teal)"/><path d="M1 2.5l5 4 5-4" stroke="#fff" stroke-width="1" fill="none"/></svg>
        hello@brivoracollective.com
      </li>
      <li>
        <svg viewBox="0 0 12 12"><circle cx="6" cy="6" r="5.3" fill="none" stroke="var(--teal)" stroke-width="1.2"/><ellipse cx="6" cy="6" rx="2.2" ry="5.3" fill="none" stroke="var(--teal)"/><line x1="0.7" y1="6" x2="11.3" y2="6" stroke="var(--teal)"/></svg>
        www.brivoracollective.com
      </li>
    </ul>
    <p class="contact-address">No.123, Street, City<br>Country</p>
  </div>
</section>

</body>
</html>
```